VerdaTurfix - 11" x 4" Door Hanger, full color both sides

We need a door hanger designed, 11" x 4", full color both sides, We are a lawn care company that provides lawn mowing, and other services to clients. This door hanger will be place on the 9 neighbors of our current clients. The ad needs to state that we provided lawn service to one of their neighbors today, and that we are in their neighborhood each week on that day. The door hanger will have 4 printings, substituting the day of Tuesday, Wednesday, Thursday, and Friday. All the art work and text will remain the same except the day of the week. For information about VerdaTurfix, please visit our website www.verdaturfix.net. The main emphasis of the message should be that we are their every week on that day, and the benefits to them of using our service (ie. quality time with their family, golf, sports, resting, etc., instead of mowing the lawn). At the bottom of the door hanger will be a coupon offering their tenth (10th) lawn service free, which is the same as a 10% discount.

I have uploaded a template files for the front and back of an 11 x 4 door hanger, The templates are pdf, jpeg, or eps files. The final product can be a pdf, jpeg, or eps file.

Target Market(s)

Neighbors of our existing clients

Industry/Entity Type

Lawn Care

Font styles to use
Serif

Requirements
Must have
• Professional design and art, Short conversational message that relays the following thoughts:
• 1. We mowed your neighbor's lawn today!
• 2. We are in your neighborhood every Tuesday!
• 3. Our lawn service is guaranteed.
• 4. Call to action - Call us today! 555-014-7382
• 5. Of course our contact info, name, phone number, website address.
• 6. Coupon at bottom for "10th lawn service Free!"
Nice to have
• Art work from our website is fine to use, That carries our theme throughout our campaign.
Should not have
• Very wordy. This is basically a billboard, Have very few seconds to grab their attention.

```html
<!DOCTYPE html>
<html lang="en">
<head>
<meta charset="utf-8">
<title>VerdaTurfix Door Hanger</title>
<link rel="stylesheet" href="https://fonts.googleapis.com/css2?family=Oswald:wght@400;500&family=Montserrat:wght@400;500;700&display=swap">
<style>
  :root {
    --ink: #0d0d0d;
    --red: #e53b3b;
    --white: #ffffff;
    --backdrop: #ece9e4;
    --grass-dark: #3f7a22;
    --grass-light: #8cc63f;
    --foliage: #5f8b3a;
  }
  * { box-sizing: border-box; margin: 0; padding: 0; }
  html, body { width: 1200px; height: 1000px; overflow: hidden; background: var(--backdrop); }
  .canvas { position: relative; width: 1200px; height: 1000px; }
  .hanger { position: absolute; top: 42px; height: 918px; }
  .hanger--front { left: 183px; width: 378px; }
  .hanger--back { left: 637px; width: 382px; }
  .hanger__art { position: absolute; inset: 0; width: 100%; height: 100%; display: block; }

  .headline-box {
    position: absolute; border: 1px dashed rgba(255,255,255,.85); border-radius: 7px;
    color: var(--white); font-family: "Oswald", sans-serif; text-transform: uppercase;
    text-align: center; display: flex; flex-direction: column; justify-content: center;
  }
  .headline-box--front { left: 52px; top: 241px; width: 278px; height: 72px; font-size: 25px; line-height: 31px; }
  .headline-box--front .accent { font-size: 32px; }
  .headline-box--back { left: 39px; top: 242px; width: 304px; height: 57px; font-size: 16px; line-height: 23px; }
  .accent { color: var(--red); }

  .schedule { position: absolute; left: 0; width: 100%; text-align: center; font-family: "Oswald", sans-serif; }
  .schedule__lead { top: 670px; font-size: 20px; color: var(--ink); }
  .schedule__day { top: 700px; font-size: 37px; color: var(--red); font-weight: 500; }

  .guarantee-bar {
    position: absolute; left: 36px; top: 755px; width: 308px; height: 22px; background: var(--red);
    border-radius: 3px; color: var(--white); font-family: "Oswald", sans-serif; font-size: 15px;
    line-height: 22px; text-align: center; text-transform: uppercase;
  }

  .contact-panel {
    position: absolute; left: 29px; top: 796px; width: 323px; height: 122px; background: var(--ink);
    border-radius: 14px 14px 0 0; text-align: center; font-family: "Montserrat", sans-serif; color: var(--white);
    padding-top: 10px;
  }
  .brand-name { font-family: "Montserrat", sans-serif; font-weight: 700; text-transform: uppercase; letter-spacing: .5px; }
  .contact-panel .brand-name { font-size: 25px; line-height: 30px; }
  .call-line { font-size: 14px; line-height: 18px; }
  .phone { color: var(--red); font-weight: 500; letter-spacing: 1px; }
  .contact-panel .phone { font-size: 29px; line-height: 36px; }

  .contact-block { position: absolute; left: 0; top: 668px; width: 100%; text-align: center; font-family: "Montserrat", sans-serif; color: var(--ink); }
  .contact-block .brand-name { font-size: 31px; line-height: 38px; }
  .contact-block .call-line { font-size: 16px; line-height: 20px; color: #333; }
  .contact-block .phone { font-size: 31px; line-height: 36px; font-weight: 700; }
  .contact-block .web { font-size: 17px; line-height: 24px; font-weight: 500; }

  .coupon {
    position: absolute; left: 43px; top: 810px; width: 295px; height: 68px; background: var(--red);
    border-radius: 9px; display: flex; align-items: center; justify-content: center; gap: 10px; color: var(--white);
  }
  .coupon::before { content: ""; position: absolute; inset: 4px; border: 1px dashed rgba(255,255,255,.8); border-radius: 7px; }
  .coupon__label { font-family: "Oswald", sans-serif; font-size: 20px; line-height: 22px; text-align: center; }
  .coupon__offer { font-family: "Montserrat", sans-serif; font-weight: 700; font-size: 50px; line-height: 1; letter-spacing: 1px; }
</style>
</head>
<body>
<main class="canvas">

  <section class="hanger hanger--front">
    <svg class="hanger__art" viewBox="0 0 378 918" preserveAspectRatio="none">
      <defs>
        <linearGradient id="front-scene" x1="0" y1="0" x2="1" y2="1">
          <stop offset="0" stop-color="#a7b98a"/>
          <stop offset=".5" stop-color="var(--foliage)"/>
          <stop offset="1" stop-color="var(--grass-dark)"/>
        </linearGradient>
      </defs>
      <rect width="378" height="918" fill="var(--white)"/>
      <rect width="378" height="380" fill="var(--ink)"/>
      <path d="M0 345 C120 322 260 322 378 335 L378 660 C260 680 120 662 0 620 Z" fill="var(--red)"/>
      <path role="img" aria-label="Photo of a man pushing a lawn mower across a garden lawn" d="M0 358 C120 345 260 360 378 395 L378 640 C260 650 120 620 0 560 Z" fill="url(#front-scene)"/>
      <circle cx="189" cy="153" r="58" fill="var(--backdrop)"/>
      <rect x="189" y="153" width="190" height="20" fill="var(--backdrop)"/>
    </svg>
    <div class="headline-box headline-box--front">
      <span>We mowed your</span>
      <span>Neighbor's lawn <span class="accent">Today!</span></span>
    </div>
    <p class="schedule schedule__lead">We are in your neighborhood every</p>
    <p class="schedule schedule__day">TUESDAY!</p>
    <p class="guarantee-bar">Our lawn service is guaranteed.</p>
    <div class="contact-panel">
      <p class="brand-name">VerdaTurfix!</p>
      <p class="call-line">Call us today!</p>
      <p class="phone">555-014-7382</p>
    </div>
  </section>

  <section class="hanger hanger--back">
    <svg class="hanger__art" viewBox="0 0 382 918" preserveAspectRatio="none">
      <defs>
        <linearGradient id="back-scene" x1="0" y1="0" x2="1" y2="0">
          <stop offset="0" stop-color="var(--grass-light)"/>
          <stop offset=".45" stop-color="var(--grass-dark)"/>
          <stop offset=".7" stop-color="#c83030"/>
          <stop offset="1" stop-color="#e04040"/>
        </linearGradient>
      </defs>
      <rect width="382" height="918" fill="var(--white)"/>
      <rect width="382" height="380" fill="var(--ink)"/>
      <path d="M0 350 C120 326 260 326 382 338 L382 660 C260 672 120 650 0 600 Z" fill="var(--red)"/>
      <path role="img" aria-label="Close-up photo of a red lawn mower cutting green grass" d="M0 362 C120 350 260 360 382 385 L382 648 C260 652 120 620 0 540 Z" fill="url(#back-scene)"/>
      <circle cx="190" cy="153" r="58" fill="var(--backdrop)"/>
      <rect x="190" y="158" width="193" height="16" fill="var(--backdrop)"/>
    </svg>
    <div class="headline-box headline-box--back">
      <span>Our guaranteed lawn care service and</span>
      <span>Prices <span class="accent">mow down the competition!</span></span>
    </div>
    <div class="contact-block">
      <p class="brand-name">VerdaTurfix!</p>
      <p class="call-line">Call us today!</p>
      <p class="phone">555-014-7382</p>
      <p class="web">service@verdaturfix.net</p>
      <p class="web">www.verdaturfix.net</p>
    </div>
    <div class="coupon">
      <p class="coupon__label">10th Lawn<br>Service</p>
      <p class="coupon__offer">FREE</p>
    </div>
  </section>

</main>
</body>
</html>
```